HomeBridle business card and stationary design

We are looking for a simple yet elegant design for our mortgage company business card and stationary.

The card should include:
Name (Derek Walsh)
Title (CEO)
Phone Number (614-208-3917)
Address (48 Birchfield Court, Suite 314, Marlow, OH 43952)
Email (email@homebridle-example.com)
"NMLS" i.e. (NMLS 61947)
"Company NMLS" (Company NMLS 472815)

See above

```html
<!DOCTYPE html>
<html lang="en">
<head>
<meta charset="utf-8">
<title>HomeBridle Business Card</title>
<link rel="stylesheet" href="https://fonts.googleapis.com/css2?family=Montserrat:wght@600;700&family=Arimo:wght@400&display=swap">
<style>
  :root {
    --backdrop: #2b2725;
    --card-navy: #1b2530;
    --accent-blue: #00aeef;
    --text-white: #ffffff;
  }
  * { margin: 0; padding: 0; box-sizing: border-box; }
  html, body {
    width: 1200px;
    height: 842px;
    overflow: hidden;
    background: var(--backdrop);
  }
  .canvas {
    position: relative;
    width: 1200px;
    height: 842px;
  }
  .card {
    position: absolute;
    top: 266px;
    width: 540px;
    height: 309px;
    background: var(--card-navy);
    overflow: hidden;
  }
  .card--contact { left: 40px; }
  .card--brand { left: 620px; }

  /* Contact side */
  .band {
    position: absolute;
    left: 0;
    width: 100%;
    height: 14px;
    background: var(--accent-blue);
  }
  .band--top { top: 0; }
  .band--bottom { bottom: 0; }
  .contact-block {
    position: absolute;
    left: 0;
    right: 0;
    top: 58px;
    text-align: center;
    font-family: "Arimo", Arial, sans-serif;
    color: var(--text-white);
    font-size: 14px;
    line-height: 18px;
  }
  .contact-name {
    font-family: "Montserrat", sans-serif;
    font-weight: 700;
    font-size: 25px;
    line-height: 28px;
    color: var(--accent-blue);
  }
  .contact-title { font-size: 15px; line-height: 18px; }
  .divider {
    width: 90px;
    height: 1px;
    margin: 9px auto;
    background: var(--accent-blue);
  }
  .web-domain { color: var(--accent-blue); }

  /* Brand side */
  .tab {
    position: absolute;
    width: 30px;
    height: 62px;
    background: var(--accent-blue);
  }
  .tab--left { left: 0; top: 150px; }
  .tab--right { right: 0; top: 62px; }
  .brand-name {
    position: absolute;
    left: 0;
    right: 0;
    top: 98px;
    text-align: center;
    font-family: "Montserrat", sans-serif;
    font-weight: 600;
    font-size: 54px;
    line-height: 60px;
    color: var(--text-white);
  }
  .license-line {
    position: absolute;
    left: 0;
    right: 0;
    top: 196px;
    text-align: center;
    font-family: "Arimo", Arial, sans-serif;
    font-size: 14px;
    color: var(--text-white);
  }
  .license-label { color: var(--accent-blue); }
  .license-sep { margin: 0 8px; color: var(--text-white); }
</style>
</head>
<body>
<main class="canvas">
  <section class="card card--contact">
    <div class="band band--top"></div>
    <div class="contact-block">
      <p class="contact-name">Derek Walsh</p>
      <p class="contact-title">CEO</p>
      <div class="divider"></div>
      <p>614-208-3917</p>
      <p>email@homebridle-example.com</p>
      <p>www.<span class="web-domain">homebridle</span>.com</p>
      <div class="divider"></div>
      <p>48 Birchfield Court, Suite 314</p>
      <p>Marlow, OH 43952</p>
    </div>
    <div class="band band--bottom"></div>
  </section>

  <section class="card card--brand">
    <div class="tab tab--right"></div>
    <div class="tab tab--left"></div>
    <p class="brand-name">HomeBridle</p>
    <p class="license-line">
      <span class="license-label">NMLS</span> 61947<span class="license-sep">|</span><span class="license-label">Company NMLS</span> 472815
    </p>
  </section>
</main>
</body>
</html>
```